Professional Facebook Banner, Business Cards, Door Hang Tags, Service Flyer for Pest Control Company

There are really 4 things I need designed but Pixel Harbor doesn't have them to package together. I am needing to get a Professional Facebook Banner, Business Cards, Door Hang Tags, and Service Flyer for a Pest Control Company. I already have a logo that I will attach to the project along with content a for each one of these tasks. Please see document attached labeled All Design Content & Flyer Content.
Pest Control

```html
<!DOCTYPE html>
<html lang="en">
<head>
<meta charset="utf-8">
<title>Citrus Grove Pest Control – Brand Set</title>
<link href="https://fonts.googleapis.com/css2?family=Montserrat:wght@400;600;700;800;900&family=Varela+Round&family=Roboto+Condensed:wght@500;700&display=swap" rel="stylesheet">
<style>
  :root{
    --orange:#f26a2e;
    --orange-deep:#c9501c;
    --gold:#f4b400;
    --amber:#e8921c;
    --black:#0b0b0b;
    --white:#ffffff;
    --bronze:#b0703a;
    --silver:#a9a9a9;
    --gold-card:#e3b410;
  }
  *{box-sizing:border-box;margin:0;padding:0}
  html,body{width:1200px;height:2181px;overflow:hidden;background:var(--white)}
  body{position:relative;font-family:"Montserrat",sans-serif;color:var(--white)}
  .panel{position:absolute;overflow:hidden}
  .brand{font-family:"Montserrat",sans-serif;font-weight:900;color:var(--orange);text-transform:uppercase;line-height:1;letter-spacing:.02em;position:relative;z-index:2}

  /* pest target icons */
  .pest-grid{position:absolute;display:grid;z-index:2}
  .pest-item{display:flex;flex-direction:column;align-items:center;text-align:center;font-weight:700;text-transform:uppercase;line-height:1.1;color:var(--white)}
  .pest{width:var(--s);height:var(--s);border-radius:50%;border:2px solid var(--orange);position:relative;flex:none;
        background:radial-gradient(circle,var(--orange) 0 36%,transparent 38%)}
  .pest::before,.pest::after{content:"";position:absolute;background:var(--orange)}
  .pest::before{left:-16%;right:-16%;top:50%;height:1.5px;margin-top:-.75px}
  .pest::after{top:-16%;bottom:-16%;left:50%;width:1.5px;margin-left:-.75px}

  /* ---------- business card scene ---------- */
  .card-scene{left:0;top:0;width:867px;height:609px;background:radial-gradient(ellipse at 50% 40%,#484848,#262626)}
  .card{position:absolute;width:350px;height:200px;background:var(--black);overflow:hidden;box-shadow:0 14px 30px rgba(0,0,0,.55)}
  .card-front{left:110px;top:110px}
  .card-back{left:420px;top:310px}
  .card svg.swoosh{position:absolute;inset:0}
  .card-front .brand{position:absolute;left:24px;top:26px;font-size:18px}
  .card-name{position:absolute;left:44px;top:78px;font-size:15px;font-weight:700;color:var(--orange)}
  .card-role{position:absolute;left:44px;top:96px;font-size:10px}
  .card-contact{position:absolute;left:24px;top:120px;font-size:10px;line-height:17px}
  .card-contact span{display:inline-block;width:9px;height:9px;border-radius:50%;background:var(--orange);margin-right:10px;vertical-align:-1px}
  .card-bar{position:absolute;left:0;right:60px;bottom:16px;height:32px;background:var(--orange);display:flex;align-items:center;padding-left:24px;font-size:16px;font-weight:700;gap:10px}
  .phone-dot{width:18px;height:18px;border-radius:50%;background:var(--white);display:inline-flex;flex:none}
  .card-back-band{position:absolute;left:70px;top:14px;width:220px;height:22px;background:var(--orange);border-radius:0 11px 11px 0;font-size:10px;font-weight:700;display:flex;align-items:center;justify-content:center}
  .card-back .pest-grid{left:28px;top:54px;grid-template-columns:repeat(5,58px);row-gap:10px;font-size:6.5px}
  .card-back .pest{--s:28px;margin-bottom:4px}

  /* ---------- social banner ---------- */
  .social-banner{left:0;top:616px;width:867px;height:328px;background:var(--black)}
  .social-banner .pest-grid{left:81px;top:96px;grid-template-columns:repeat(5,60px);row-gap:12px;font-size:7.5px}
  .social-banner .pest{--s:44px;margin-bottom:10px}
  .social-banner .brand{position:absolute;left:516px;top:132px;font-size:20px}
  .banner-phone{position:absolute;left:516px;top:180px;font-size:19px;font-weight:700;display:flex;align-items:center;gap:8px}

  /* ---------- service flyer ---------- */
  .flyer{left:0;top:952px;width:867px;height:1229px;background:var(--black)}
  .flyer-photo{position:absolute;left:0;top:0;width:867px;height:760px;
    background:radial-gradient(ellipse at 62% 35%,#6b6b6b 0,#3a3a3a 45%,#111 85%)}
  .flyer-photo-tint{position:absolute;left:0;top:0;width:867px;height:760px;background:linear-gradient(90deg,rgba(0,0,0,.75),rgba(0,0,0,.25))}
  .flyer svg.swoosh{position:absolute;left:0;top:0}
  .flyer .brand{position:absolute;left:80px;top:52px;font-size:44px}
  .flyer-intro{position:absolute;left:81px;top:183px;width:720px;font-family:"Varela Round",sans-serif;font-size:25px;line-height:32px;text-align:justify}
  .flyer-intro.accent{top:370px;color:var(--gold)}
  .flyer .pest-grid{left:75px;top:494px;grid-template-columns:repeat(5,86px);row-gap:12px;font-size:11.5px;font-weight:600}
  .flyer .pest{--s:52px;margin-bottom:12px}
  .plan{position:absolute;top:738px;width:248px;height:398px;border-radius:20px;font-family:"Roboto Condensed",sans-serif;font-weight:500;font-size:15.5px;line-height:20px;text-align:center;color:#2a1505;padding-top:102px}
  .plan-bronze{left:44px;background:linear-gradient(180deg,rgba(30,30,30,.85) 0,rgba(176,112,58,.95) 45%,var(--bronze))}
  .plan-silver{left:310px;background:linear-gradient(180deg,rgba(50,50,50,.85) 0,#bdbdbd 45%,var(--silver));color:#1d1d1d}
  .plan-gold{left:576px;background:linear-gradient(180deg,rgba(60,45,0,.85) 0,#eec21a 45%,var(--gold-card));color:#2a1d00}
  .plan-badge{position:absolute;left:66px;top:-24px;width:116px;height:116px;border-radius:50%;display:flex;align-items:center;justify-content:center;text-align:center;font-family:"Montserrat",sans-serif;font-weight:900;font-size:15px;line-height:18px;color:#2a1505;text-transform:uppercase}
  .plan-bronze .plan-badge{background:radial-gradient(circle at 35% 30%,#e8a36a,#a35f2a)}
  .plan-silver .plan-badge{background:radial-gradient(circle at 35% 30%,#f2f2f2,#8d8d8d);color:#1d1d1d}
  .plan-gold .plan-badge{background:radial-gradient(circle at 35% 30%,#ffe45a,#c99700);color:#2a1d00}
  .plan ul{list-style:none}
  .plan .extra{color:var(--white)}
  .price-box{position:absolute;left:30px;right:30px;bottom:16px;height:26px;border-radius:6px;background:#f3ece4;color:#222;font-size:13px;text-align:left;padding:4px 30px}
  .flyer-note{position:absolute;left:60px;top:1170px;width:760px;text-align:center;font-weight:800;font-size:11px;line-height:15px}

  /* ---------- door hangers ---------- */
  .hanger{left:876px;width:324px;height:753px;background:linear-gradient(150deg,#f6c21a 0,#e79a1a 45%,#d06a14 100%)}
  .hanger-about{top:0}
  .hanger-services{top:762px}
  .hanger svg.swoosh{position:absolute;left:0;top:0}
  .hanger-hole{position:absolute;left:115px;width:96px;height:96px;border-radius:50%;background:var(--white)}
  .hanger-slit{position:absolute;height:9px;background:var(--white)}
  .hanger-about .hanger-hole{top:73px}
  .hanger-about .hanger-slit{left:0;width:140px;top:116px}
  .hanger-services .hanger-hole{top:62px}
  .hanger-services .hanger-slit{left:180px;width:144px;top:116px}
  .hanger-about .brand{position:absolute;left:42px;top:222px;font-size:22px}
  .hanger-copy{position:absolute;left:41px;top:290px;width:243px;font-size:11.6px;line-height:15px;text-align:justify;font-weight:600}
  .hanger-copy p+p{margin-top:15px}
  .hanger-cta{position:absolute;left:38px;top:514px;font-size:18.5px;font-weight:700;color:var(--orange)}
  .hanger-phone{position:absolute;left:38px;top:540px;font-size:28px;font-weight:700;display:flex;align-items:center;gap:8px}
  .hanger-web{position:absolute;left:38px;top:576px;font-size:14px;font-weight:700;display:flex;align-items:center;gap:8px}
  .dot{width:14px;height:14px;border-radius:50%;background:var(--orange);flex:none}
  .offer{position:absolute;left:0;width:324px;text-align:center;z-index:2}
  .offer-amount{font-size:31px;font-weight:900;color:var(--orange);line-height:1}
  .offer-title{font-size:15.5px;font-weight:700;margin-top:4px}
  .offer-fine{font-size:10px;font-weight:700}
  .hanger-about .offer{top:648px}
  .hanger-services .offer{top:652px}
  .hanger-band{position:absolute;left:38px;top:203px;width:249px;height:35px;background:var(--orange);border-radius:0 0 14px 14px;font-size:13px;font-weight:700;display:flex;align-items:center;justify-content:center}
  .hanger-services .pest-grid{left:68px;top:270px;grid-template-columns:repeat(3,63px);row-gap:14px;font-size:8px}
  .hanger-services .pest{--s:46px;margin-bottom:8px}
</style>
</head>
<body>

<!-- business cards -->
<section class="panel card-scene">
  <article class="card card-front">
    <svg class="swoosh" width="350" height="200" viewBox="0 0 350 200">
      <defs><linearGradient id="cardArc" x1="0" x2="1"><stop offset="0" stop-color="#2a1205"/><stop offset="1" stop-color="#f26a2e"/></linearGradient></defs>
      <path d="M200 0 Q330 40 310 200 L350 200 L350 0 Z" fill="url(#cardArc)"/>
      <path d="M240 0 Q350 50 335 200 L350 200 L350 0Z" fill="#e8921c"/>
    </svg>
    <div class="brand">Citrus Grove<br>Pest Control</div>
    <div class="card-name">Evan Marlow</div>
    <div class="card-role">Owner</div>
    <div class="card-contact"><span></span>evan@citrusgrovepest.com<br><span></span>www.citrusgrovepest.com</div>
    <div class="card-bar"><span class="phone-dot"></span>555-014-2870</div>
  </article>
  <article class="card card-back">
    <svg class="swoosh" width="350" height="200" viewBox="0 0 350 200">
      <path d="M230 0 Q350 70 300 200 L350 200 L350 0Z" fill="#c9501c"/>
      <path d="M275 0 Q360 80 330 200 L350 200 L350 0Z" fill="#e8921c"/>
    </svg>
    <div class="card-back-band">SERVICES / INSPECTIONS</div>
    <div class="pest-grid">
      <div class="pest-item"><div class="pest" role="img" aria-label="Ant icon"></div>Ants</div>
      <div class="pest-item"><div class="pest" role="img" aria-label="Mosquito icon"></div>Mosquitos</div>
      <div class="pest-item"><div class="pest" role="img" aria-label="Flea icon"></div>Fleas</div>
      <div class="pest-item"><div class="pest" role="img" aria-label="Roach icon"></div>Roaches</div>
      <div class="pest-item"><div class="pest" role="img" aria-label="Wasp icon"></div>Stinging Insects</div>
      <div class="pest-item"><div class="pest" role="img" aria-label="Spider icon"></div>Spiders</div>
      <div class="pest-item"><div class="pest" role="img" aria-label="Rodent icon"></div>Rodents</div>
      <div class="pest-item"><div class="pest" role="img" aria-label="Termite icon"></div>Termites</div>
      <div class="pest-item"><div class="pest" role="img" aria-label="Mouse icon"></div>Mice</div>
      <div class="pest-item"><div class="pest" role="img" aria-label="Rat icon"></div>Rats</div>
    </div>
  </article>
</section>

<!-- social banner -->
<section class="panel social-banner">
  <svg class="swoosh" width="867" height="328" viewBox="0 0 867 328" style="position:absolute;left:0;top:0">
    <defs><linearGradient id="bannerGold" x1="0" y1="0" x2="1" y2="1"><stop offset="0" stop-color="#f6c21a"/><stop offset="1" stop-color="#d9791a"/></linearGradient>
      <linearGradient id="bannerArc" x1="0" x2="1"><stop offset="0" stop-color="#000"/><stop offset="1" stop-color="#f26a2e"/></linearGradient></defs>
    <rect x="430" y="0" width="437" height="328" fill="url(#bannerGold)"/>
    <path d="M430 0 L600 0 Q830 70 770 328 L430 328 Z" fill="url(#bannerArc)"/>
    <path d="M0 0 L560 0 Q790 100 720 328 L0 328 Z" fill="#0b0b0b"/>
  </svg>
  <div class="pest-grid">
    <div class="pest-item"><div class="pest" role="img" aria-label="Ant icon"></div>Ants</div>
    <div class="pest-item"><div class="pest" role="img" aria-label="Mosquito icon"></div>Mosquitos</div>
    <div class="pest-item"><div class="pest" role="img" aria-label="Flea icon"></div>Fleas</div>
    <div class="pest-item"><div class="pest" role="img" aria-label="Roach icon"></div>Roaches</div>
    <div class="pest-item"><div class="pest" role="img" aria-label="Wasp icon"></div>Stinging Insects</div>
    <div class="pest-item"><div class="pest" role="img" aria-label="Spider icon"></div>Spiders</div>
    <div class="pest-item"><div class="pest" role="img" aria-label="Rodent icon"></div>Rodents</div>
    <div class="pest-item"><div class="pest" role="img" aria-label="Termite icon"></div>Termites</div>
    <div class="pest-item"><div class="pest" role="img" aria-label="Mouse icon"></div>Mice</div>
    <div class="pest-item"><div class="pest" role="img" aria-label="Rat icon"></div>Rats</div>
  </div>
  <div class="brand">Citrus Grove<br>Pest Control</div>
  <div class="banner-phone"><span class="phone-dot"></span>555-014-2870</div>
</section>

<!-- service flyer -->
<section class="panel flyer">
  <div class="flyer-photo" role="img" aria-label="Technician in protective suit spraying pest treatment inside a home"></div>
  <div class="flyer-photo-tint"></div>
  <svg class="swoosh" width="867" height="1229" viewBox="0 0 867 1229">
    <defs><linearGradient id="flyerGold" x1="0" y1="0" x2="1" y2="1"><stop offset="0" stop-color="#f28a1e"/><stop offset=".6" stop-color="#f4b400"/><stop offset="1" stop-color="#d87a14"/></linearGradient></defs>
    <path d="M0 560 Q250 760 520 700 Q760 640 867 480 L867 1229 L0 1229 Z" fill="url(#flyerGold)"/>
    <path d="M0 640 Q300 840 560 760 Q780 690 867 520 L867 620 Q780 790 560 860 Q280 930 0 720Z" fill="#f26a2e"/>
    <path d="M0 860 Q0 1140 250 1160 Q500 1180 867 1100 L867 1229 L0 1229 Z" fill="#0b0b0b"/>
  </svg>
  <div class="brand">Citrus Grove<br>Pest Control</div>
  <p class="flyer-intro">Pests are constantly trying to enter your home, which can easily cause frustration and damage to your home and belongings. That's why we at Citrus Grove Pest Control provide seasonally designed, proactive home pest control plans to your family and your home.</p>
  <p class="flyer-intro accent">Our home pest control plans offer effective and affordable solutions to all your pest issues in and around your home. If you have pest problems,</p>
  <div class="pest-grid">
    <div class="pest-item"><div class="pest" role="img" aria-label="Ant icon"></div>Ants</div>
    <div class="pest-item"><div class="pest" role="img" aria-label="Mosquito icon"></div>Mosquitos</div>
    <div class="pest-item"><div class="pest" role="img" aria-label="Flea icon"></div>Fleas</div>
    <div class="pest-item"><div class="pest" role="img" aria-label="Roach icon"></div>Roaches</div>
    <div class="pest-item"><div class="pest" role="img" aria-label="Wasp icon"></div>Stinging Insects</div>
    <div class="pest-item"><div class="pest" role="img" aria-label="Spider icon"></div>Spiders</div>
    <div class="pest-item"><div class="pest" role="img" aria-label="Rodent icon"></div>Rodents</div>
    <div class="pest-item"><div class="pest" role="img" aria-label="Termite icon"></div>Termites</div>
    <div class="pest-item"><div class="pest" role="img" aria-label="Mouse icon"></div>Mice</div>
    <div class="pest-item"><div class="pest" role="img" aria-label="Rat icon"></div>Rats</div>
  </div>

  <article class="plan plan-bronze">
    <div class="plan-badge">Home<br>Defense<br>Bronze</div>
    <ul>
      <li>Year-Round Pest Protection</li><li>Bi-Monthly Service (6 visits per year)</li><li>Covers 15+ Pests</li><li>Exterior Treatment</li><li>Interior Treatment (As Needed)</li><li>Rodent Control</li><li>Stinging Insect Removal</li><li>Free Re-Treatments</li>
    </ul>
    <div class="price-box">$______________</div>
  </article>
  <article class="plan plan-silver">
    <div class="plan-badge">Home<br>Defense<br>Silver</div>
    <ul>
      <li>Year-Round Pest Protection</li><li>Bi-Monthly Service (6 visits per year)</li><li>Covers 15+ Pests</li><li>Exterior Treatment</li><li>Interior Treatment (As Needed)</li><li>Rodent Control</li><li>Stinging Insect Removal</li><li>Free Re-Treatments</li>
      <li class="extra">+</li><li class="extra">Termite Monitoring</li>
    </ul>
    <div class="price-box">$______________</div>
  </article>
  <article class="plan plan-gold">
    <div class="plan-badge">Home<br>Defense<br>Gold</div>
    <ul>
      <li>Home Defense Gold</li><li>Year-Round Pest Protection</li><li>Bi-Monthly Service (6 visits per year)</li><li>Covers 15+ Pests</li><li>Exterior Treatment</li><li>Interior Treatment (As Needed)</li><li>Rodent Control</li><li>Stinging Insect Removal</li><li>Free Re-Treatments</li>
      <li class="extra">+</li><li class="extra">Termite Monitoring &amp;</li><li class="extra">Mosquito Reduction Treatments</li>
    </ul>
    <div class="price-box">$______________</div>
  </article>

  <p class="flyer-note">Please Note: to have full guarantee for Asian Beetles, Brown Recluse Spider, Cluster Flies, Lady Bugs, and Silverfish the structures attic and/or crawlspace would need to be treated. There are additional fees for theses services</p>
</section>

<!-- door hanger: about -->
<section class="panel hanger hanger-about">
  <svg class="swoosh" width="324" height="753" viewBox="0 0 324 753">
    <path d="M0 240 Q10 120 160 100 Q310 110 324 200 L324 615 Q250 650 140 645 Q20 635 0 590Z" fill="#c9501c"/>
    <path d="M0 250 Q20 140 165 125 Q320 135 324 230 L324 595 Q250 632 140 627 Q20 617 0 565Z" fill="#0b0b0b"/>
  </svg>
  <div class="hanger-slit"></div>
  <div class="hanger-hole"></div>
  <div class="brand">Citrus Grove<br>Pest Control</div>
  <div class="hanger-copy">
    <p>We are a locally owned and operated, with 10 years of industry experience our family is committed to delivering exceptional customer service and high-quality results. We strive for excellence in all that we do.</p>
    <p>We treat each and every customer like a member of our family. When you partner with us, you can enjoy hassle-free services, expert care, and peace of mind knowing you and your home are protected from pests for years to come.</p>
  </div>
  <div class="hanger-cta">Call Now for a Free Quote</div>
  <div class="hanger-phone"><span class="dot"></span>(555) 014-2870</div>
  <div class="hanger-web"><span class="dot"></span>www.citrusgrovepest.com</div>
  <div class="offer">
    <div class="offer-amount">$50 OFF</div>
    <div class="offer-title">Initial Home Protection Plan</div>
    <div class="offer-fine">New Customers Only</div>
  </div>
</section>

<!-- door hanger: services -->
<section class="panel hanger hanger-services">
  <svg class="swoosh" width="324" height="753" viewBox="0 0 324 753">
    <path d="M0 230 Q20 120 165 110 Q310 120 324 220 L324 590 Q260 640 140 635 Q20 625 0 565Z" fill="#c9501c"/>
    <path d="M0 245 Q25 140 165 130 Q315 140 324 245 L324 565 Q250 620 140 615 Q25 605 0 540Z" fill="#0b0b0b"/>
  </svg>
  <div class="hanger-slit"></div>
  <div class="hanger-hole"></div>
  <div class="hanger-band">SERVICES / INSPECTIONS</div>
  <div class="pest-grid">
    <div class="pest-item"><div class="pest" role="img" aria-label="Ant icon"></div>Ants</div>
    <div class="pest-item"><div class="pest" role="img" aria-label="Mosquito icon"></div>Mosquitos</div>
    <div class="pest-item"><div class="pest" role="img" aria-label="Wasp icon"></div>Stinging Insects</div>
    <div class="pest-item"><div class="pest" role="img" aria-label="Spider icon"></div>Spiders</div>
    <div class="pest-item"><div class="pest" role="img" aria-label="Rodent icon"></div>Rodents</div>
    <div class="pest-item"><div class="pest" role="img" aria-label="Rat icon"></div>Rats</div>
    <div class="pest-item"><div class="pest" role="img" aria-label="Flea icon"></div>Fleas</div>
    <div class="pest-item"><div class="pest" role="img" aria-label="Roach icon"></div>Roaches</div>
    <div class="pest-item"></div>
    <div class="pest-item"><div class="pest" role="img" aria-label="Termite icon"></div>Termites</div>
    <div class="pest-item"><div class="pest" role="img" aria-label="Mouse icon"></div>Mice</div>
  </div>
  <div class="offer">
    <div class="offer-amount">$25 OFF</div>
    <div class="offer-title">One Time Service</div>
    <div class="offer-fine">New Customers Only</div>
  </div>
</section>

</body>
</html>
```